Business Card For Life Coaching Business For Men

Take my existing logo and apply it to a business card. I would like the logo to be prominent with stylistic text below reading Life Coaching For Men. Contact info should show as:
Gideon Marsh
gideon@bravepathgrowth.com

```html
<!DOCTYPE html>
<html lang="en">
<head>
<meta charset="utf-8">
<title>Brave Path Growth – Business Card</title>
<link href="https://fonts.googleapis.com/css2?family=Barlow+Condensed:wght@400;500;600;700&display=swap" rel="stylesheet">
<style>
  :root {
    --backdrop: #d4d5d7;
    --navy: #2b2f7c;
    --teal: #058585;
    --teal-text: #13808a;
    --white: #ffffff;
    --faint: #e6e4ef;
  }
  * { margin: 0; padding: 0; box-sizing: border-box; }
  html, body {
    width: 900px;
    height: 1200px;
    overflow: hidden;
    background: var(--backdrop);
    font-family: "Barlow Condensed", "Arial Narrow", sans-serif;
  }
  .card {
    position: absolute;
    left: 134px;
    width: 632px;
    height: 364px;
    overflow: hidden;
  }
  .card--front {
    top: 210px;
    background: linear-gradient(to bottom, var(--navy), var(--teal));
    color: var(--white);
  }
  .card--back {
    top: 624px;
    background: var(--white);
  }

  /* Front */
  .front-mark {
    position: absolute;
    left: 276px;
    top: 318px;
  }
  .front-mark { left: 142px; top: 108px; }
  .front-brand {
    position: absolute;
    left: 302px;
    top: 108px;
  }
  .front-brand__name {
    font-weight: 600;
    font-size: 58px;
    line-height: 0.98;
    letter-spacing: 0.5px;
    text-transform: uppercase;
  }
  .front-brand__tagline {
    margin-top: 12px;
    font-weight: 600;
    font-size: 18px;
    letter-spacing: 1.6px;
    text-transform: uppercase;
  }

  /* Back */
  .back-decoration {
    position: absolute;
    left: 330px;
    top: 24px;
  }
  .back-brand {
    position: absolute;
    left: 32px;
    top: 42px;
    display: flex;
    align-items: center;
    gap: 14px;
  }
  .back-brand__name {
    color: var(--navy);
    font-weight: 600;
    font-size: 38px;
    line-height: 0.98;
    text-transform: uppercase;
  }
  .contact {
    position: absolute;
    left: 134px;
    top: 210px;
    color: var(--navy);
  }
  .contact__name {
    color: var(--teal-text);
    font-weight: 700;
    font-size: 24px;
    letter-spacing: 0.5px;
    text-transform: uppercase;
    line-height: 1;
  }
  .contact__role {
    margin-top: 4px;
    font-size: 16px;
    font-weight: 500;
  }
  .contact__list {
    list-style: none;
    margin-top: 8px;
  }
  .contact__item {
    display: flex;
    align-items: center;
    gap: 8px;
    font-size: 17px;
    font-weight: 500;
    height: 23px;
  }
  .contact__icon { width: 15px; height: 15px; flex: none; }
</style>
</head>
<body>

<section class="card card--front" aria-label="Business card front">
  <svg class="front-mark" width="140" height="140" viewBox="0 0 140 140" aria-hidden="true">
    <circle cx="70" cy="70" r="62" fill="none" stroke="var(--white)" stroke-width="10"/>
  </svg>
  <div class="front-brand">
    <div class="front-brand__name">Brave Path<br>Growth</div>
    <div class="front-brand__tagline">Life Coaching for Men</div>
  </div>
</section>

<section class="card card--back" aria-label="Business card back">
  <svg class="back-decoration" width="310" height="310" viewBox="0 0 310 310" aria-hidden="true">
    <circle cx="155" cy="155" r="140" fill="none" stroke="var(--faint)" stroke-width="20"/>
  </svg>

  <div class="back-brand">
    <svg width="80" height="80" viewBox="0 0 80 80" aria-hidden="true">
      <circle cx="40" cy="40" r="34" fill="none" stroke="var(--navy)" stroke-width="7"/>
    </svg>
    <div class="back-brand__name">Brave Path<br>Growth</div>
  </div>

  <div class="contact">
    <div class="contact__name">Gideon Marsh</div>
    <div class="contact__role">Owner</div>
    <ul class="contact__list">
      <li class="contact__item">
        <svg class="contact__icon" viewBox="0 0 16 16" aria-hidden="true">
          <path d="M3.2 1.5l2.4-.3 1.6 3.4-1.6 1.3c.9 2 2.4 3.5 4.4 4.4l1.3-1.6 3.4 1.6-.3 2.4c-.2.8-.9 1.3-1.7 1.3C7 14 2 9 2 3.2c0-.8.5-1.5 1.2-1.7z" fill="var(--teal)"/>
        </svg>
        <span>(555)014-2296</span>
      </li>
      <li class="contact__item">
        <svg class="contact__icon" viewBox="0 0 16 16" aria-hidden="true">
          <rect x="1" y="3" width="14" height="10" fill="var(--teal)"/>
          <path d="M1.5 3.5L8 9l6.5-5.5M1.5 12.5l4.5-4.5M14.5 12.5L10 8" fill="none" stroke="var(--white)" stroke-width="1.2"/>
        </svg>
        <span>gideon@bravepathgrowth.com</span>
      </li>
      <li class="contact__item">
        <svg class="contact__icon" viewBox="0 0 16 16" aria-hidden="true">
          <g fill="none" stroke="var(--teal)" stroke-width="1.4">
            <circle cx="8" cy="8" r="6.5"/>
            <ellipse cx="8" cy="8" rx="3" ry="6.5"/>
            <path d="M1.5 8h13M2.5 4.8h11M2.5 11.2h11"/>
          </g>
        </svg>
        <span>www.bravepathgrowth.com</span>
      </li>
    </ul>
  </div>
</section>

</body>
</html>
```